Business card for a Exhibition booth fabrication company

Hi. My company would like to change our corporate name card. We are an events and Exhibition stand builder company. We would like our corporate name card to resonate what we do. I need someone to create something unique that relates to the industry that I am in. The graphic designer should be creative to incorporate the elements of my industry and try to blend in well in the design of the card. Our aim is to ensure that we are unique and our card can look different from our competitors.
Updates

The decision maker was very busy and didnt had time to make this decision

Target Market(s)

Marketing and events manager from all companies

Contact Information for Business Card

The business card should have the following details:
Name
Job Title
Email
Website

Colors

Designer to choose colors to be used in the design.

Requirements
Must have
• The card must be look something that is relevant to the service that I am providing. My website is: www.velmora-buildworks.example
• You can see my website to get more information on what service that I am doing
Nice to have
• On the back of my card, I would like to have a globe image with the incorporation of my company logo. This is to indicate that my services can be done in any part of the world.

```html
<!DOCTYPE html>
<html lang="en">
<head>
<meta charset="utf-8">
<title>Velmora Buildworks – Business Card</title>
<link rel="stylesheet" href="https://fonts.googleapis.com/css2?family=Lato:wght@400;700&display=swap">
<style>
  :root {
    --backdrop: #222222;
    --card-white: #fbfbfb;
    --card-dark: #1c1c1c;
    --brand-red: #e42228;
    --ink: #333333;
    --ink-soft: #555555;
    --band-dark: #1a1a1a;
    --globe-light: #4a4a4a;
    --globe-dark: #262626;
  }
  * { margin: 0; padding: 0; box-sizing: border-box; }
  html, body {
    width: 980px; height: 1200px; overflow: hidden;
    background: var(--backdrop);
    font-family: "Lato", sans-serif;
  }
  .canvas { position: relative; width: 980px; height: 1200px; }
  .card {
    position: absolute; left: 126px; width: 756px; height: 432px; overflow: hidden;
  }
  .card-front { top: 101px; background: var(--card-white); }
  .card-back { top: 641px; background: var(--card-dark); }

  .front-brand {
    position: absolute; left: 40px; width: 340px; top: 150px;
    display: flex; flex-direction: column; align-items: center; gap: 18px;
  }
  .brand-dot { width: 46px; height: 46px; border-radius: 50%; background: var(--brand-red); }
  .brand-name {
    font-weight: 700; font-size: 23px; letter-spacing: 2px; color: var(--ink-soft);
    text-transform: uppercase; white-space: nowrap;
  }
  .divider {
    position: absolute; left: 412px; top: 120px; width: 1.5px; height: 188px; background: var(--ink);
  }
  .contact-block { position: absolute; left: 438px; top: 114px; }
  .person-name { font-size: 33px; font-weight: 400; color: var(--brand-red); line-height: 1.05; }
  .person-title { font-size: 17px; color: var(--ink); letter-spacing: 0.5px; margin-top: 2px; }
  .contact-list { list-style: none; margin-top: 22px; }
  .contact-list li {
    display: flex; align-items: center; gap: 10px;
    font-size: 17px; color: var(--ink); letter-spacing: 0.5px; height: 29.5px;
  }
  .contact-list svg { width: 14px; height: 14px; flex: none; fill: var(--brand-red); }
  .band { position: absolute; left: 0; bottom: 0; width: 756px; height: 18px; }

  .globe {
    position: absolute; left: 188px; top: 26px; width: 380px; height: 380px; border-radius: 50%;
    background: radial-gradient(circle at 70% 40%, var(--globe-light), var(--globe-dark) 75%);
  }
  .back-brand {
    position: absolute; left: 0; right: 0; top: 196px; text-align: center;
    font-weight: 700; font-size: 34px; letter-spacing: 3px; color: var(--brand-red);
    text-transform: uppercase;
  }
</style>
</head>
<body>
<main class="canvas">
  <section class="card card-front">
    <div class="front-brand">
      <span class="brand-dot"></span>
      <span class="brand-name">Velmora Buildworks</span>
    </div>
    <div class="divider"></div>
    <div class="contact-block">
      <h1 class="person-name">Daniel Harlow</h1>
      <p class="person-title">Founder &amp; CEO</p>
      <ul class="contact-list">
        <li><svg viewBox="0 0 24 24"><path d="M6.6 10.8c1.4 2.8 3.8 5.1 6.6 6.6l2.2-2.2c.3-.3.7-.4 1-.2 1.1.4 2.3.6 3.6.6.6 0 1 .4 1 1V20c0 .6-.4 1-1 1C10.6 21 3 13.4 3 4c0-.6.4-1 1-1h3.5c.6 0 1 .4 1 1 0 1.3.2 2.5.6 3.6.1.3 0 .7-.2 1z"/></svg>+65 81047726 (Singapore)</li>
        <li><svg viewBox="0 0 24 24"><path d="M6.6 10.8c1.4 2.8 3.8 5.1 6.6 6.6l2.2-2.2c.3-.3.7-.4 1-.2 1.1.4 2.3.6 3.6.6.6 0 1 .4 1 1V20c0 .6-.4 1-1 1C10.6 21 3 13.4 3 4c0-.6.4-1 1-1h3.5c.6 0 1 .4 1 1 0 1.3.2 2.5.6 3.6.1.3 0 .7-.2 1z"/></svg>+974 55208143 (Qatar)</li>
        <li><svg viewBox="0 0 24 24"><path d="M2 5h20v2l-10 6L2 7z"/><path d="M2 9.3l10 6 10-6V19H2z"/></svg>info@velmora-buildworks.example</li>
        <li><svg viewBox="0 0 24 24" fill="none"><g fill="none" stroke="#e42228" stroke-width="2"><circle cx="12" cy="12" r="9"/><ellipse cx="12" cy="12" rx="4" ry="9"/><path d="M3 12h18M5 7h14M5 17h14"/></g></svg>www.velmora-buildworks.example</li>
      </ul>
    </div>
    <svg class="band" viewBox="0 0 756 18" preserveAspectRatio="none">
      <polygon points="0,0 394,0 378,18 0,18" fill="var(--brand-red)"/>
      <polygon points="394,0 402,0 386,18 378,18" fill="#ffffff"/>
      <polygon points="402,0 756,0 756,18 386,18" fill="var(--band-dark)"/>
    </svg>
  </section>

  <section class="card card-back">
    <div class="globe" role="img" aria-label="Globe with world map showing continents in grey"></div>
    <p class="back-brand">Velmora Buildworks</p>
  </section>
</main>
</body>
</html>
```